professional business card design

Business card design. Photos have been uploaded and i am open to the designer choosing which photos to use. Would like the card to be mostyly in a grey scale design with black, whites, silver & grey colours. I have added copy of our flyer as would like on the back side of card our services to be listed. Do not use any bright colurs such as blue red green or yellow. i need to be able to edit the phone number and naem in the final card design submitted.

Target Market(s)

Clients

Industry/Entity Type

earhmovibng and transport

Contact Information for Business Card

Director Name, address, email, phone number and services

Colors

Designer to choose only greyscale colors for use in the design.

Requirements
Should not have
• no yellow, red, blue or green

```html
<!DOCTYPE html>
<html lang="en">
<head>
<meta charset="utf-8">
<title>RCT Pty Ltd – Business Card</title>
<link rel="stylesheet" href="https://fonts.googleapis.com/css2?family=Arimo:wght@400;700&display=swap">
<style>
  :root {
    --page-bg: #8a7d6c;
    --card-black: #0b0b0b;
    --card-dark: #1c1c1c;
    --silver-light: #f4f4f4;
    --silver-mid: #c9c9c9;
    --silver-dark: #8c8c8c;
    --text-dark: #111111;
    --text-light: #ffffff;
    --text-grey: #555555;
    --logo-grey: #b8b8b8;
  }
  * { margin: 0; padding: 0; box-sizing: border-box; }
  html, body { width: 900px; height: 1200px; overflow: hidden; }
  body {
    position: relative;
    background: var(--page-bg);
    font-family: "Arimo", Arial, sans-serif;
  }
  .card {
    position: absolute;
    left: 78px;
    width: 745px;
    height: 443px;
    border-radius: 24px;
    overflow: hidden;
    background: var(--card-black);
    box-shadow: 0 6px 14px rgba(0,0,0,.45);
  }
  .card--front { top: 130px; }
  .card--back { top: 638px; }

  .brand-name {
    position: absolute;
    font-weight: 700;
    color: var(--logo-grey);
    letter-spacing: 4px;
    line-height: 1;
  }
  .card--front .brand-name { left: 38px; top: 40px; font-size: 82px; }

  .truck-photo {
    position: absolute;
    left: 352px; top: 18px;
    width: 393px; height: 360px;
    background: linear-gradient(160deg, #d9dcdf 0%, #a9adb1 45%, #3a3b3d 100%);
    border-radius: 8px 0 0 8px;
  }

  .name-band {
    position: absolute;
    left: 0; top: 225px;
    width: 440px; height: 54px;
    background: linear-gradient(90deg, var(--silver-light) 0%, var(--silver-mid) 60%, rgba(200,200,200,0) 100%);
    padding: 6px 0 0 26px;
  }
  .person-name { font-size: 24px; font-weight: 700; color: var(--text-dark); letter-spacing: .3px; }
  .person-role { font-size: 14px; font-weight: 700; color: var(--text-grey); margin-top: 1px; }

  .contact-list {
    position: absolute;
    left: 26px; top: 302px;
    list-style: none;
    color: var(--text-light);
    font-size: 16px;
  }
  .contact-list li { display: flex; align-items: center; height: 23px; }
  .contact-list svg { width: 14px; height: 14px; margin-right: 16px; fill: var(--text-light); }

  .address-band {
    position: absolute;
    left: 0; bottom: 16px;
    width: 100%; height: 30px;
    background: linear-gradient(90deg, var(--silver-light), var(--silver-mid) 70%, var(--silver-dark));
    color: var(--text-dark);
    font-size: 16px; font-weight: 700;
    padding: 5px 0 0 26px;
    letter-spacing: .3px;
  }

  .back-panel {
    position: absolute;
    left: 0; top: 0; width: 100%; height: 274px;
    background: radial-gradient(ellipse at 50% 40%, #3a3a3a 0%, #1a1a1a 55%, #080808 100%);
  }
  .card--back .brand-name {
    left: 0; width: 100%; top: 60px;
    text-align: center; font-size: 130px; letter-spacing: 10px;
  }
  .company-suffix {
    position: absolute;
    left: 0; width: 100%; top: 216px;
    text-align: center;
    font-size: 30px; font-weight: 700;
    color: var(--logo-grey);
  }
  .services-band {
    position: absolute;
    left: 0; top: 274px; width: 100%; height: 44px;
    background: linear-gradient(90deg, var(--silver-mid), var(--silver-light) 50%, var(--silver-mid));
    text-align: center;
    font-size: 24px; font-weight: 700;
    color: var(--text-dark);
    padding-top: 9px;
  }
  .services-list {
    position: absolute;
    left: 0; top: 326px; width: 100%;
    color: var(--text-light);
    font-size: 15px;
    text-align: center;
    line-height: 27px;
  }
  .services-list .sep { margin: 0 10px; }
</style>
</head>
<body>

<section class="card card--front">
  <div class="brand-name">RCT</div>
  <div class="truck-photo" role="img" aria-label="Photo of a white prime mover truck with oversize sign"></div>

  <div class="name-band">
    <div class="person-name">DANIEL REEVE</div>
    <div class="person-role">Director</div>
  </div>

  <ul class="contact-list">
    <li><svg viewBox="0 0 24 24"><path d="M3 9c0-3 4-5 9-5s9 2 9 5l-4 1-1-3H8L7 10 3 9zm3 3h12l2 8H4l2-8zm6 2a2 2 0 1 0 0 4 2 2 0 0 0 0-4z"/></svg>000 444 000</li>
    <li><svg viewBox="0 0 24 24"><path d="M2 5h20v14H2zM3 6l9 7 9-7v2l-9 7-9-7z"/></svg>info@redrockhaulage.com.au</li>
    <li><svg viewBox="0 0 24 24"><circle cx="12" cy="12" r="10"/></svg>www.redrockhaulage.com.au</li>
  </ul>

  <div class="address-band">DEPOT : RCT LOT 41, QUARRY GATE ROAD, STONEHAVEN, AUSTRALIA</div>
</section>

<section class="card card--back">
  <div class="back-panel" role="img" aria-label="Dark perforated metal texture"></div>
  <div class="brand-name">RCT</div>
  <div class="company-suffix">Pty Ltd</div>
  <div class="services-band">OUR SERVICES</div>
  <div class="services-list">
    <p>Mine site accredited equipment &amp; operators<span class="sep">|</span>Drop Deck Trailers<span class="sep">|</span>Road train flat tops</p>
    <p>Road train Tankers<span class="sep">|</span>Road train Tippers<span class="sep">|</span>Sand &amp; Metal Supply &amp; cartage<span class="sep">|</span>Earthworks</p>
    <p>Road Building / Maintenance<span class="sep">|</span>potable water delivers<span class="sep">|</span>Heavy Vehicle Recovery services</p>
    <p>Over size load / Hot Shot Load</p>
  </div>
</section>

</body>
</html>
```